Brand refresh of quote, work docket and Fire certificate documents

I would like a refresh of our document suit including

1. Front page called VOLT3 Proposal
2. Quote document template
3. Work docket template
4. Fire certificate template - to look like a professional complaint certificate

Examples of documents are attached.

```html
<!DOCTYPE html>
<html lang="en">
<head>
<meta charset="utf-8">
<title>VOLT3 Document Suite</title>
<link rel="stylesheet" href="https://fonts.googleapis.com/css2?family=Montserrat:wght@300;400;500;800&display=swap">
<style>
:root{
  --bg:#e2e2e2;
  --paper:#ffffff;
  --ink:#1e1e1e;
  --brand-dark:#3a3a3a;
  --brand-red:#c8202c;
  --brand-orange:#ef6a1f;
  --grey-mid:#707070;
  --band-dark:#3d3d3d;
  --faint:#f1f1f1;
}
*{margin:0;padding:0;box-sizing:border-box}
html,body{width:1200px;height:1200px;overflow:hidden}
body{background:var(--bg);font-family:"Montserrat",sans-serif;color:var(--ink);position:relative}
.page{position:absolute;width:392px;height:554px;background:var(--paper);box-shadow:4px 6px 10px rgba(0,0,0,.18);overflow:hidden}
.logo{position:absolute;left:47px;top:50px;display:flex;align-items:center;gap:4px;font-weight:800;font-size:26px;letter-spacing:-.5px;color:var(--brand-dark);line-height:1}
.logo-dot{width:7px;height:7px;background:var(--brand-orange)}
.address{font-size:5.8px;line-height:8.5px;font-weight:500;color:var(--ink)}
.address-top{position:absolute;right:47px;top:46px;text-align:right}
.address-foot{position:absolute;left:47px;top:477px}

/* certificate */
.cert-frame{position:absolute;inset:16px;border:2px solid var(--ink)}
.cert-frame::after{content:"";position:absolute;inset:2px;border:.8px solid var(--ink)}
.cert-title{position:absolute;left:48px;top:108px;font-weight:800;font-size:19.5px;color:var(--brand-red);white-space:nowrap}
.cert-line{position:absolute;left:47px;font-size:7.8px;line-height:14.4px;white-space:nowrap}
.cert-line .label{display:inline-block}
.cert-number{color:var(--brand-red)}
.seal{position:absolute;left:57px;top:153px;width:280px;height:280px;border-radius:50%;border:9px solid rgba(200,32,44,.06);background:rgba(0,0,0,.035)}
.signature{position:absolute;left:82px;top:418px;width:63px;height:25px;background:#ececec}
.watermark{position:absolute;left:44px;top:410px;font-weight:800;font-size:104px;letter-spacing:-3px;color:var(--faint);line-height:1}

/* cover sheets */
.proposal-word{position:absolute;left:137px;top:44px;font-size:34px;font-weight:500;color:var(--grey-mid);letter-spacing:-.5px;line-height:1}
.title-band{position:absolute;left:145px;right:0;top:48px;height:29px;background:linear-gradient(90deg,#ffffff 0%,#bdbdbd 45%,var(--band-dark) 100%)}
.band-word{position:absolute;right:19px;top:47px;font-size:29px;font-weight:300;line-height:30px;letter-spacing:-.5px}
.band-word.quote{color:#d6d6d6}
.band-word.docket{color:#333333}
</style>
</head>
<body>

<!-- Certificate, seal version -->
<section class="page certificate" style="left:100px;top:30px">
  <div class="cert-frame"></div>
  <div class="seal" aria-hidden="true"></div>
  <div class="logo"><span class="logo-dot"></span>VOLT3</div>
  <div class="address address-top">VOLT3 Pty Ltd<br>4/21 Marlow Street<br>Eastfield VIC 3188<br>admin@volt3.com.au</div>
  <h1 class="cert-title">Fire/Smoke System Certificate</h1>
  <p class="cert-line" style="top:140px"><span class="label" style="width:40px">Client:</span>Northgate Compliance Group</p>
  <p class="cert-line" style="top:160px"><span class="label" style="width:40px">Job:</span>Larkin Court 18-26 Ellery Road, Brambleton – Building 4</p>
  <p class="cert-line" style="top:180px"><span class="label" style="width:80px">Certificate Number:</span><span class="cert-number">2262</span></p>
  <p class="cert-line" style="top:199px;line-height:11.8px"><span class="label" style="width:46px">Reference:</span>Fire/smoke sealing of your various service penetrations<br><span class="label" style="width:46px"></span>as detailed below</p>
  <p class="cert-line" style="top:243px">VOLT3 Pty. Ltd. certifies that as part of our contracted works, we have carried<br>out the above fire protection at Larkin Court 18-26 Ellery Road, Brambleton –<br>Building 4 as instructed by Priya Halden of Northgate Compliance Group.</p>
  <p class="cert-line" style="top:299px">These works have been completed and checked using the approved<br>proprietary fire resistance tested products &amp; systems as per AS1530 part 4<br>&amp; AS4072 part 1<br>Any works that are modified, damaged or disturbed following completion<br>are not covered by this certification.</p>
  <p class="cert-line" style="top:381px">Installed in accordance with the manufacturer’s specifications.</p>
  <p class="cert-line" style="top:428px">Signed:</p>
  <div class="signature" role="img" aria-label="Handwritten signature"></div>
  <p class="cert-line" style="top:452px"><span class="label" style="width:34px">Name:</span>Dale Whitcombe</p>
  <p class="cert-line" style="top:476px"><span class="label" style="width:34px">Date:</span>30th January, 2026</p>
</section>

<!-- Certificate, watermark version -->
<section class="page certificate" style="left:100px;top:615px">
  <div class="cert-frame"></div>
  <div class="watermark" aria-hidden="true">VOLT3</div>
  <div class="logo"><span class="logo-dot"></span>VOLT3</div>
  <div class="address address-top">VOLT3 Pty Ltd<br>4/21 Marlow Street<br>Eastfield VIC 3188<br>admin@volt3.com.au</div>
  <h1 class="cert-title">Fire/Smoke System Certificate</h1>
  <p class="cert-line" style="top:140px"><span class="label" style="width:40px">Client:</span>Northgate Compliance Group</p>
  <p class="cert-line" style="top:160px"><span class="label" style="width:40px">Job:</span>Larkin Court 18-26 Ellery Road, Brambleton – Building 4</p>
  <p class="cert-line" style="top:180px"><span class="label" style="width:80px">Certificate Number:</span><span class="cert-number">2262</span></p>
  <p class="cert-line" style="top:199px;line-height:11.8px"><span class="label" style="width:46px">Reference:</span>Fire/smoke sealing of your various service penetrations<br><span class="label" style="width:46px"></span>as detailed below</p>
  <p class="cert-line" style="top:243px">VOLT3 Pty. Ltd. certifies that as part of our contracted works, we have carried<br>out the above fire protection at Larkin Court 18-26 Ellery Road, Brambleton –<br>Building 4 as instructed by Priya Halden of Northgate Compliance Group.</p>
  <p class="cert-line" style="top:299px">These works have been completed and checked using the approved<br>proprietary fire resistance tested products &amp; systems as per AS1530 part 4<br>&amp; AS4072 part 1<br>Any works that are modified, damaged or disturbed following completion<br>are not covered by this certification.</p>
  <p class="cert-line" style="top:381px">Installed in accordance with the manufacturer’s specifications.</p>
  <p class="cert-line" style="top:428px">Signed:</p>
  <div class="signature" role="img" aria-label="Handwritten signature"></div>
  <p class="cert-line" style="top:452px">Name: Dale Whitcombe</p>
  <p class="cert-line" style="top:476px">Date: 30th January, 2026</p>
</section>

<!-- Proposal cover -->
<section class="page proposal" style="left:522px;top:73px">
  <div class="logo"><span class="logo-dot"></span>VOLT3</div>
  <div class="proposal-word">PROPOSAL</div>
  <div class="address address-foot">VOLT3 Pty Ltd<br>4/21 Marlow Street<br>Eastfield VIC 3188<br>admin@volt3.com.au</div>
</section>

<!-- Quotation template -->
<section class="page quotation" style="left:647px;top:336px">
  <div class="title-band"></div>
  <div class="band-word quote">QUOTATION</div>
  <div class="logo"><span class="logo-dot"></span>VOLT3</div>
  <div class="address address-foot">VOLT3 Pty Ltd<br>4/21 Marlow Street<br>Eastfield VIC 3188<br>admin@volt3.com.au</div>
</section>

<!-- Work docket template -->
<section class="page workdocket" style="left:769px;top:573px">
  <div class="title-band"></div>
  <div class="band-word docket">WORKDOCKET</div>
  <div class="logo"><span class="logo-dot"></span>VOLT3</div>
  <div class="address address-foot">VOLT3 Pty Ltd<br>4/21 Marlow Street<br>Eastfield VIC 3188<br>admin@volt3.com.au</div>
</section>

</body>
</html>
```